Varnell Skyworks Limited

Started a consulting business 12 months ago and have since moved location and have grown and seek to identify my self to the industry.
Specializing in quality solutions, business documentation and maintenance solution's

Industry/Entity Type

Business

```html
<!DOCTYPE html>
<html lang="en">
<head>
<meta charset="utf-8">
<title>Varnell Skyworks Limited – Business Card</title>
<link rel="stylesheet" href="https://fonts.googleapis.com/css2?family=Roboto+Condensed:wght@700&family=Open+Sans:wght@400&family=Tinos&display=swap">
<style>
  :root {
    --orange: #f7a035;
    --slate: #52646a;
    --grey-text: #7a7a7a;
    --divider: #9a9a9a;
    --paper: #ffffff;
  }
  html, body {
    margin: 0;
    padding: 0;
    overflow: hidden;
    background: var(--paper);
  }
  .card {
    position: relative;
    width: 1200px;
    height: 635px;
    background: var(--paper);
    overflow: hidden;
  }
  .corner {
    position: absolute;
  }
  .corner--top-left { left: 0; top: 0; }
  .corner--bottom-right { right: 0; bottom: 0; }

  .divider {
    position: absolute;
    left: 589px;
    top: 98px;
    width: 2px;
    height: 445px;
    background: var(--divider);
  }

  /* Left: company block */
  .brand {
    position: absolute;
    right: 736px;
    top: 140px;
    width: 460px;
    text-align: right;
  }
  .brand__mark {
    display: inline-block;
    width: 64px;
    height: 64px;
    background: var(--slate);
    border-radius: 8px;
    margin-bottom: 58px;
  }
  .brand__name {
    margin: 0;
    font-family: "Roboto Condensed", "Arial Narrow", sans-serif;
    font-weight: 700;
    font-size: 39px;
    line-height: 1;
    color: var(--slate);
    white-space: nowrap;
  }
  .brand__tagline {
    margin: 24px 0 0;
    font-family: "Open Sans", Arial, sans-serif;
    font-size: 25px;
    line-height: 39px;
    color: var(--grey-text);
  }

  /* Right: contact block */
  .contact {
    position: absolute;
    left: 647px;
    top: 132px;
    font-family: "Tinos", "Times New Roman", serif;
    font-size: 32px;
    line-height: 1.3;
  }
  .contact__name { margin: 0; color: var(--slate); }
  .contact__role { margin: 0; color: var(--orange); }
  .contact__group { margin: 64px 0 0 10px; }
  .contact__group + .contact__group { margin-top: 34px; }
  .contact__label { margin: 0; color: var(--slate); }
  .contact__value { margin: 0; color: var(--orange); }
  .contact__value--email { margin-left: -6px; }
</style>
</head>
<body>
  <main class="card">
    <svg class="corner corner--top-left" width="106" height="106" viewBox="0 0 106 106" aria-hidden="true">
      <path d="M0 3H106M3 0V106" stroke="var(--orange)" stroke-width="7" fill="none"/>
    </svg>
    <svg class="corner corner--bottom-right" width="106" height="106" viewBox="0 0 106 106" aria-hidden="true">
      <path d="M0 103H106M103 0V106" stroke="var(--orange)" stroke-width="7" fill="none"/>
    </svg>

    <section class="brand">
      <span class="brand__mark" aria-hidden="true"></span>
      <h1 class="brand__name">Varnell Skyworks Limited</h1>
      <p class="brand__tagline">Specializing in quality solutions<br>business documentation and<br>maintenance solution's</p>
    </section>

    <div class="divider" aria-hidden="true"></div>

    <section class="contact">
      <p class="contact__name">Idris Calloway</p>
      <p class="contact__role">Owner and Chief strategist</p>
      <div class="contact__group">
        <p class="contact__label">Mobile</p>
        <p class="contact__value">+974&nbsp; 55018237</p>
      </div>
      <div class="contact__group">
        <p class="contact__label">E-mail</p>
        <p class="contact__value contact__value--email">idriscalloway42@varnellsky.com</p>
      </div>
    </section>
  </main>
</body>
</html>
```